Tova Brisk Fitness Coaching Project

I am a personal trainer based in London. My services include one-on-one PT sessions, bootcamps.
I would like the design to be minimalistic. With light colours: white, pink, purple.
I specialise in weight loss, flexibility, mobility.

Tova Penrick
Personal Trainer
Email: tova.penrick@mailgrove.net
tel: 07500 918 243
Instagram: Tova Brisk

Target Market(s)

adults, mostly females (age 18-50).

Industry/Entity Type

Fitness

Contact Information for Business Card

Tova Penrick
Personal Trainer
tel: 07500 918 243
Instagram: Tova Brisk

Font styles to use
Serif

Colors
eea4c8
fbd4d5
fdf9cf
cfeae6
cee9f5

Requirements
Nice to have
• minimalistic style
• easy to read and remember

```html
<!DOCTYPE html>
<html lang="en">
<head>
<meta charset="utf-8">
<title>Tova Penrick – Personal Trainer Business Card</title>
<link rel="stylesheet" href="https://fonts.googleapis.com/css2?family=Quicksand:wght@500;600;700&display=swap">
<style>
  :root {
    --backdrop: #29bfcc;
    --card: #ffffff;
    --ink: #111111;
    --pink: #e4127f;
    --magenta: #b52e8f;
    --teal: #2bb8c6;
    --navy: #2b3990;
    --indigo: #3f51a5;
    --yellow: #f7e61c;
    --orange: #f7941d;
    --plum: #2e1a5e;
    --slate: #3a3f44;
  }
  * { margin: 0; padding: 0; box-sizing: border-box; }
  html, body {
    width: 1200px; height: 1200px; overflow: hidden;
    background: var(--backdrop);
    font-family: "Quicksand", sans-serif;
    color: var(--ink);
  }
  .card {
    position: absolute;
    width: 840px; height: 480px;
    background: var(--card);
    overflow: hidden;
  }
  .card--back { left: 54px; top: 80px; }
  .card--front { left: 298px; top: 620px; }
  .card__art { position: absolute; inset: 0; width: 840px; height: 480px; }
  .identity { position: absolute; }
  .identity__name { font-weight: 600; line-height: 1; white-space: nowrap; }
  .identity__role { font-weight: 500; line-height: 1; white-space: nowrap; }
  .card--back .identity { left: 553px; top: 96px; }
  .card--back .identity__name { font-size: 35px; }
  .card--back .identity__role { font-size: 18px; margin-top: 12px; }
  .card--front .identity { left: 563px; top: 100px; }
  .card--front .identity__name { font-size: 45px; }
  .card--front .identity__role { font-size: 19px; margin-top: 13px; }
  .contacts { position: absolute; left: 553px; top: 242px; list-style: none; }
  .contacts__item {
    display: flex; align-items: center; gap: 15px;
    height: 16px; margin-bottom: 32px;
    font-size: 14px; font-weight: 600; white-space: nowrap;
  }
  .contacts__icon { width: 14px; height: 14px; flex: none; }
</style>
</head>
<body>
<svg width="0" height="0" style="position:absolute" aria-hidden="true">
  <defs>
    <linearGradient id="photo-tones" x1="0" y1="0" x2="0" y2="1">
      <stop offset="0" stop-color="#e4127f"/>
      <stop offset="0.33" stop-color="#e8307f"/>
      <stop offset="0.42" stop-color="#2bb8c6"/>
      <stop offset="0.7" stop-color="#30b5c2"/>
      <stop offset="0.82" stop-color="#3a3f44"/>
      <stop offset="1" stop-color="#2c3034"/>
    </linearGradient>
    <linearGradient id="g-sun" x1="0" y1="0" x2="0" y2="1">
      <stop offset="0" stop-color="#f7e61c"/><stop offset="1" stop-color="#f7941d"/>
    </linearGradient>
    <linearGradient id="g-sunset" x1="0" y1="1" x2="0" y2="0">
      <stop offset="0" stop-color="#f7e61c"/><stop offset="0.6" stop-color="#f7941d"/><stop offset="1" stop-color="#f26a21"/>
    </linearGradient>
    <linearGradient id="g-dusk" x1="0" y1="0" x2="0" y2="1">
      <stop offset="0" stop-color="#f7941d"/><stop offset="0.45" stop-color="#8a4a6a"/><stop offset="1" stop-color="#2e1a5e"/>
    </linearGradient>
    <linearGradient id="g-deep" x1="0" y1="0" x2="0" y2="1">
      <stop offset="0" stop-color="#2b3990"/><stop offset="1" stop-color="#4556a8"/>
    </linearGradient>
    <linearGradient id="g-berry" x1="0" y1="0" x2="0" y2="1">
      <stop offset="0" stop-color="#d6358f"/><stop offset="1" stop-color="#9c2a8a"/>
    </linearGradient>
    <linearGradient id="g-lagoon" x1="0" y1="0" x2="0" y2="1">
      <stop offset="0" stop-color="#2bb8c6"/><stop offset="0.5" stop-color="#a06a96"/><stop offset="1" stop-color="#e4127f"/>
    </linearGradient>
    <path id="blob" d="M0,-58 C34,-60 58,-34 56,4 C54,38 30,58 -4,58 C-38,58 -58,34 -56,-2 C-54,-36 -32,-56 0,-58Z"/>
  </defs>
</svg>

<section class="card card--back">
  <svg class="card__art" viewBox="0 0 840 480">
    <polygon points="186,38 372,252 186,468 0,252" fill="url(#photo-tones)" stroke="url(#photo-tones)" stroke-width="10" stroke-linejoin="round" role="img" aria-label="Photo of the trainer leaping in front of a pink and teal painted wall"/>
    <use href="#blob" transform="translate(12,88) scale(1,0.9)" fill="url(#g-deep)"/>
    <use href="#blob" transform="translate(298,8) scale(1.15,1.05)" fill="url(#g-sun)"/>
    <use href="#blob" transform="translate(448,136) scale(0.98,0.9)" fill="url(#g-dusk)"/>
    <use href="#blob" transform="translate(413,420) scale(0.9,0.9)" fill="url(#g-deep)"/>
    <use href="#blob" transform="translate(12,470) scale(1,0.95)" fill="url(#g-berry)"/>
    <use href="#blob" transform="translate(796,478) scale(1.25,0.95)" fill="url(#g-sunset)"/>
  </svg>
  <div class="identity">
    <h1 class="identity__name">Tova Penrick</h1>
    <p class="identity__role">Personal Trainer</p>
  </div>
  <ul class="contacts">
    <li class="contacts__item">
      <svg class="contacts__icon" viewBox="0 0 14 14" aria-hidden="true"><path d="M1 5 C1 2 13 2 13 5 L10.5 6 L10 4.5 C8 4 6 4 4 4.5 L3.5 6 Z M3.5 7 L10.5 7 L12 12 L2 12 Z" fill="#111"/><circle cx="7" cy="9.3" r="1.4" fill="#fff"/></svg>
      <span>07500 918 243</span>
    </li>
    <li class="contacts__item">
      <svg class="contacts__icon" viewBox="0 0 14 14" aria-hidden="true"><rect x="1" y="3" width="12" height="8.5" fill="#111"/><path d="M1.5 3.6 L7 8 L12.5 3.6 M1.5 11 L5.5 7 M12.5 11 L8.5 7" stroke="#fff" stroke-width="1" fill="none"/></svg>
      <span>tova.penrick@mailgrove.net</span>
    </li>
    <li class="contacts__item">
      <svg class="contacts__icon" viewBox="0 0 14 14" aria-hidden="true"><rect x="1.5" y="1.5" width="11" height="11" rx="1" fill="#111"/></svg>
      <span>Tova Brisk</span>
    </li>
  </ul>
</section>

<section class="card card--front">
  <svg class="card__art" viewBox="0 0 840 480">
    <path d="M0,0 L414,0 L540,240 Q548,256 536,270 L370,480 L0,480 Z" fill="url(#photo-tones)" role="img" aria-label="Photo of the trainer leaping in front of a pink and teal painted wall"/>
    <use href="#blob" transform="translate(12,90) scale(1,0.9)" fill="url(#g-deep)"/>
    <use href="#blob" transform="translate(297,8) scale(1.15,1.05)" fill="url(#g-sun)"/>
    <use href="#blob" transform="translate(447,136) scale(0.98,0.9)" fill="url(#g-dusk)"/>
    <use href="#blob" transform="translate(782,236) scale(0.98,0.9)" fill="url(#g-lagoon)"/>
    <use href="#blob" transform="translate(414,420) scale(0.92,0.92)" fill="url(#g-deep)"/>
    <use href="#blob" transform="translate(12,470) scale(1,0.95)" fill="url(#g-berry)"/>
    <use href="#blob" transform="translate(796,478) scale(1.25,0.95)" fill="url(#g-sunset)"/>
  </svg>
  <div class="identity">
    <h2 class="identity__name">Tova Penrick</h2>
    <p class="identity__role">Personal Trainer</p>
  </div>
</section>
</body>
</html>
```